LOGO for A Neighborhood Finance Center
BLUE LEDGER PLUS
Professional
HAROLD QUINCE and DENNIS HOLTBERG
Manger
3710 S Wexford st 204
Fernbrook GA 30999
BlueLEDGERPLUS@mailnook.example
BLUELEDGERPLUS.example
I need two versions one with Harold Quince
I need one with Dennis Holtberg

```html
<!DOCTYPE html>
<html lang="en">
<head>
<meta charset="utf-8">
<title>Blue Ledger Plus — Business Card</title>
<link href="https://fonts.googleapis.com/css2?family=Open+Sans:wght@400;600;700&display=swap" rel="stylesheet">
<style>
  :root {
    --page-bg: #2b2d30;
    --brand-blue: #1f64a6;
    --deep-blue: #0d3f78;
    --mid-blue: #2a7fc4;
    --light-blue: #4a9ad6;
    --brand-green: #52b54a;
    --paper: #ffffff;
    --ink-white: #f4f8fc;
  }
  * { margin: 0; padding: 0; box-sizing: border-box; }
  html, body {
    width: 1200px; height: 901px; overflow: hidden;
    background: var(--page-bg);
    font-family: "Open Sans", Arial, sans-serif;
  }
  .canvas { position: relative; width: 1200px; height: 901px; }
  .card {
    position: absolute; left: 240px; width: 720px; height: 410px;
    border-radius: 26px; overflow: hidden;
  }
  .card-back {
    top: 30px;
    background: linear-gradient(135deg, var(--light-blue) 0%, var(--brand-blue) 45%, var(--deep-blue) 100%);
    display: flex; align-items: center; justify-content: center; gap: 14px;
  }
  .card-back .wordmark { color: var(--paper); font-size: 46px; font-weight: 700; letter-spacing: 0.5px; }
  .card-back .mark-dot { width: 18px; height: 18px; border-radius: 50%; background: var(--paper); }
  .card-back .back-web {
    position: absolute; bottom: 60px; left: 0; right: 0; text-align: center;
    color: rgba(255,255,255,0.55); font-size: 15px; letter-spacing: 3px;
  }
  .card-front { top: 461px; background: var(--paper); }
  .card-front .shape { position: absolute; inset: 0; }
  .front-logo {
    position: absolute; top: 62px; left: 0; right: 0;
    display: flex; align-items: center; justify-content: center; gap: 12px;
  }
  .front-logo .wordmark { color: var(--brand-blue); font-size: 42px; font-weight: 700; }
  .front-logo .mark-dot { width: 16px; height: 16px; border-radius: 50%; background: var(--brand-green); }
  .person { position: absolute; left: 60px; top: 245px; width: 280px; text-align: right; color: var(--ink-white); }
  .person .name { font-size: 24px; font-weight: 700; }
  .person .role { font-size: 15px; margin-top: 2px; opacity: 0.9; }
  .divider { position: absolute; left: 362px; top: 232px; width: 1px; height: 118px; background: rgba(255,255,255,0.7); }
  .contact { position: absolute; left: 378px; top: 228px; color: var(--ink-white); font-size: 14px; line-height: 20px; }
  .contact li { list-style: none; display: flex; align-items: center; gap: 7px; }
  .contact svg { width: 13px; height: 13px; flex: none; }
  .web { position: absolute; left: 0; right: 0; top: 364px; text-align: center; color: var(--ink-white); font-size: 15px; letter-spacing: 3px; padding-left: 120px; }
</style>
</head>
<body>
<main class="canvas">
  <section class="card card-back" aria-label="Card back">
    <span class="wordmark">Blue Ledger Plus</span>
    <span class="mark-dot"></span>
    <div class="back-web">www.blueledgerplus.example</div>
  </section>

  <section class="card card-front" aria-label="Card front">
    <svg class="shape" viewBox="0 0 720 410" preserveAspectRatio="none" aria-hidden="true">
      <defs>
        <linearGradient id="frontBlue" x1="0" y1="0" x2="1" y2="1">
          <stop offset="0" stop-color="#2a7fc4"/>
          <stop offset="0.5" stop-color="#1f64a6"/>
          <stop offset="1" stop-color="#0d3f78"/>
        </linearGradient>
      </defs>
      <path d="M0 188 C180 250 420 250 720 150 L720 410 L0 410 Z" fill="url(#frontBlue)"/>
      <path d="M0 170 C180 236 420 232 720 134 L720 150 C420 250 180 250 0 188 Z" fill="#52b54a"/>
    </svg>
    <div class="front-logo">
      <span class="wordmark">Blue Ledger Plus</span>
      <span class="mark-dot"></span>
    </div>
    <div class="person">
      <div class="name">Harold Quince</div>
      <div class="role">Manager</div>
    </div>
    <div class="divider"></div>
    <ul class="contact">
      <li>3710 S Wexford st 204</li>
      <li>Fernbrook GA 30999</li>
      <li><svg viewBox="0 0 16 16"><path fill="#fff" d="M4 1h3l1 4-2 1a9 9 0 0 0 4 4l1-2 4 1v3c0 1-1 2-2 2A13 13 0 0 1 2 3c0-1 1-2 2-2z"/></svg>5550143871</li>
      <li><svg viewBox="0 0 16 16"><rect x="2" y="2" width="12" height="12" rx="2" fill="none" stroke="#fff" stroke-width="1.6"/><path d="M5 6h6M5 9h6" stroke="#fff" stroke-width="1.4"/></svg>5550198264</li>
      <li><svg viewBox="0 0 16 16"><rect x="1" y="4" width="14" height="9" rx="1" fill="none" stroke="#fff" stroke-width="1.5"/><path d="M4 4V1h8v3" fill="none" stroke="#fff" stroke-width="1.5"/></svg>5550143871</li>
      <li><svg viewBox="0 0 16 16"><rect x="1" y="3" width="14" height="10" rx="1" fill="none" stroke="#fff" stroke-width="1.5"/><path d="M1 3l7 6 7-6" fill="none" stroke="#fff" stroke-width="1.5"/></svg>BlueLEDGERPLUS@mailnook.example</li>
    </ul>
    <div class="web">www.blueledgerplus.example</div>
  </section>
</main>
</body>
</html>
```